Steady Tending, professional newsletter for GAPH

** updated based on results so far** We need a 2 page newsletter designed on both sides of an 8.6 x 11 sheet back and front. Page one needs our logo below, name steady tending in large letters tagline of official newsletter of the academy of walk-in clinic practice volume and issue number locations It needs to include five locations for 250-400 word articles each with a spot for a picture. Page 2 needs to include contact information including address, phone number, email, twitter and facebook info below. The design need to complement out log in color, be professional with clean lines and easy to follow. We are a non profit organization dedicated to providers of urgent care medicine.

Target Market(s)

Physicians, Nurse Practitioners, Physician Assistants

Industry/Entity Type

It Professional

Requirements
Must have
• 2 pages, back and front 8.5x 11
• 5 article area 250-400 words, one image for each
• our logo
• Name: Steady Tending - page one large visible print
• Contact inf:
• Academy of Walk-in Clinic Practice
• 912 Larkfield Ave. Suite 418E
• Naperville, IL 60563
• 1 855-431-7094
• Info@gaphwalk.org
• @AcademyGAPH
Nice to have
• ease of entering info
• professional clean lines

```html
<!DOCTYPE html>
<html lang="en">
<head>
<meta charset="utf-8">
<title>Steady Tending – Newsletter</title>
<link rel="stylesheet" href="https://fonts.googleapis.com/css2?family=Open+Sans:wght@400;600;700&display=swap">
<style>
  :root {
    --backdrop: #a9aec4;
    --paper: #ffffff;
    --orange: #f7941d;
    --orange-deep: #f08a12;
    --charcoal: #3a3a3c;
    --ink: #6d6e71;
    --white: #ffffff;
  }
  * { margin: 0; padding: 0; box-sizing: border-box; }
  html, body { width: 1200px; height: 1161px; overflow: hidden; }
  body {
    background: var(--backdrop);
    font-family: "Open Sans", Arial, sans-serif;
    position: relative;
  }
  .page {
    position: absolute; top: 211px;
    width: 570px; height: 738px;
    background: var(--paper); overflow: hidden;
  }
  .page-front { left: 20px; }
  .page-back { left: 610px; }

  /* ---------- Front page ---------- */
  .top-bar { position: absolute; left: 0; top: 0; width: 570px; height: 12px; background: var(--orange); }
  .brand { position: absolute; left: 30px; top: 34px; height: 64px; display: flex; align-items: center; }
  .brand-mark { width: 40px; height: 40px; border-radius: 50%; background: var(--orange); margin-right: 14px; }
  .brand-rule { width: 2px; height: 64px; background: var(--ink); margin-right: 10px; }
  .brand-name { font-size: 15px; line-height: 1.15; color: var(--ink); letter-spacing: 1px; }
  .issue-line {
    position: absolute; right: 30px; top: 50px; text-align: right;
    font-size: 11px; line-height: 1.5; font-weight: 600; color: var(--ink);
  }
  .masthead {
    position: absolute; left: 28px; top: 110px;
    font-size: 56px; line-height: 1; font-weight: 700; color: var(--charcoal);
  }
  .tagline {
    position: absolute; left: 30px; top: 180px;
    font-size: 11px; font-weight: 700; color: var(--orange);
    letter-spacing: 1px; text-transform: uppercase;
  }
  .about { position: absolute; left: 30px; top: 214px; width: 510px; }
  .about h2 { font-size: 14px; font-weight: 700; color: var(--orange); margin-bottom: 3px; }
  .about p { font-size: 9.5px; line-height: 1.45; color: var(--ink); }
  .cover-photo {
    position: absolute; left: 0; top: 320px; width: 570px; height: 418px;
    background: linear-gradient(160deg, #e9edf2 0%, #cdd7e3 45%, #9fb1c6 100%);
  }
  .cover-bands { position: absolute; left: 0; top: 0; width: 570px; height: 738px; }
  .cover-claim {
    position: absolute; right: 24px; top: 430px; text-align: right;
    font-size: 28px; line-height: 1.05; font-weight: 700; color: var(--white);
  }
  .cover-mission {
    position: absolute; left: 30px; top: 660px;
    font-size: 19px; line-height: 1.08; font-weight: 700; color: var(--white);
  }

  /* ---------- Back page ---------- */
  .locations {
    position: absolute; left: 0; top: 0; width: 350px; height: 738px;
    background: linear-gradient(180deg, #fbfbfb 0%, #f1f3f5 55%, #fafafa 100%);
  }
  .location { position: absolute; left: 0; width: 350px; height: 130px; }
  .location-photo-frame {
    position: absolute; left: 18px; top: 0; width: 84px; height: 88px; background: var(--orange);
  }
  .location-photo {
    position: absolute; left: 6px; top: 6px; width: 72px; height: 76px;
    background: linear-gradient(135deg, #d7d5cf 0%, #b8b2a6 55%, #e8e4dc 100%);
  }
  .location-title { position: absolute; left: 116px; top: 0; font-size: 13px; font-weight: 700; color: var(--orange); }
  .location-text {
    position: absolute; left: 116px; top: 22px; width: 220px;
    font-size: 10px; line-height: 1.4; color: var(--ink);
  }
  .location-rule { position: absolute; left: 114px; top: 122px; width: 226px; height: 2px; background: var(--orange); }

  .contact-photo {
    position: absolute; left: 350px; top: 0; width: 220px; height: 738px;
    background: linear-gradient(200deg, #f4f4f4 0%, #e6e7e9 50%, #d9dadc 100%);
  }
  .contact-panel {
    position: absolute; left: 362px; top: 470px; width: 196px; height: 248px;
    background: rgba(58, 58, 60, 0.94);
    border-top: 6px solid var(--orange);
  }
  .contact-item {
    position: absolute; left: 14px; display: flex; align-items: flex-start; color: var(--white);
  }
  .contact-item svg { width: 14px; height: 14px; flex: none; margin-right: 10px; margin-top: 1px; }
  .contact-item .note { font-size: 10px; line-height: 1.45; width: 150px; }
  .contact-item.phone { font-size: 15px; font-weight: 600; align-items: center; }
  .contact-item.social { font-size: 10px; align-items: center; }
  .social-dot {
    width: 14px; height: 14px; border: 1.5px solid var(--white); border-radius: 50%;
    margin-right: 10px; flex: none;
  }
</style>
</head>
<body>

<section class="page page-front" aria-label="Newsletter page one">
  <div class="top-bar"></div>
  <div class="brand">
    <div class="brand-mark"></div>
    <div class="brand-rule"></div>
    <div class="brand-name">Academy of<br>Walk-in Clinic<br>Practice</div>
  </div>
  <div class="issue-line">Volume 1 | Issue 1</div>
  <h1 class="masthead">Steady Tending</h1>
  <p class="tagline">Official Newsletter of the Academy of Walk-in Clinic Practice</p>

  <div class="about">
    <h2>ABOUT US</h2>
    <p>Lorem ipsum dolor sit amet, consectetuer adipiscing elit. Aenean commodo ligula eget dolor. Aenean massa. Cum sociis natoque penatibus et magnis dis parturient montes, nascetur ridiculus mus. Donec quam felis, ultricies nec, pellentesque eu, pretium quis, sem. Nulla consequat massa quis enim. Donec pede justo, fringilla vel, aliquet nec, vulputate eget, arcu. In enim justo, rhoncus ut, imperdiet a, venenatis vitae, justo. Nullam</p>
  </div>

  <div class="cover-photo" role="img" aria-label="Photo of a clinician in scrubs and surgical cap, arms crossed, in a bright clinic"></div>
  <svg class="cover-bands" viewBox="0 0 570 738" aria-hidden="true">
    <polygon points="0,530 330,462 0,640" fill="var(--orange)"/>
    <polygon points="0,560 220,515 0,610" fill="var(--orange-deep)" opacity="0.6"/>
    <polygon points="0,640 570,330 570,530 290,738 0,738" fill="var(--charcoal)" opacity="0.96"/>
    <polygon points="320,738 570,550 570,576 360,738" fill="var(--orange)"/>
  </svg>
  <div class="cover-claim">We are<br>non profit<br>organization.</div>
  <div class="cover-mission">Dedicated to<br>providers of<br>urgent care medicine.</div>
</section>

<section class="page page-back" aria-label="Newsletter page two">
  <div class="locations">
    <article class="location" style="top:18px">
      <div class="location-photo-frame"><div class="location-photo" role="img" aria-label="Photo of clinic staff at location one"></div></div>
      <h3 class="location-title">LOCATION 01</h3>
      <p class="location-text">Lorem ipsum dolor sit amet, consectetuer adipiscing elit. Aenean commodo ligula eget dolor. Aenean massa. Cum sociis natoque penatibus et magnis dis parturient montes, nascetur ridiculus mus. Donec quam felis, ultricies nec,</p>
      <div class="location-rule"></div>
    </article>
    <article class="location" style="top:156px">
      <div class="location-photo-frame"><div class="location-photo" role="img" aria-label="Photo of clinic staff at location two"></div></div>
      <h3 class="location-title">LOCATION 02</h3>
      <p class="location-text">Lorem ipsum dolor sit amet, consectetuer adipiscing elit. Aenean commodo ligula eget dolor. Aenean massa. Cum sociis natoque penatibus et magnis dis parturient montes, nascetur ridiculus mus. Donec quam felis, ultricies nec,</p>
      <div class="location-rule"></div>
    </article>
    <article class="location" style="top:294px">
      <div class="location-photo-frame"><div class="location-photo" role="img" aria-label="Photo of clinic staff at location three"></div></div>
      <h3 class="location-title">LOCATION 03</h3>
      <p class="location-text">Lorem ipsum dolor sit amet, consectetuer adipiscing elit. Aenean commodo ligula eget dolor. Aenean massa. Cum sociis natoque penatibus et magnis dis parturient montes, nascetur ridiculus mus. Donec quam felis, ultricies nec,</p>
      <div class="location-rule"></div>
    </article>
    <article class="location" style="top:432px">
      <div class="location-photo-frame"><div class="location-photo" role="img" aria-label="Photo of clinic staff at location four"></div></div>
      <h3 class="location-title">LOCATION 04</h3>
      <p class="location-text">Lorem ipsum dolor sit amet, consectetuer adipiscing elit. Aenean commodo ligula eget dolor. Aenean massa. Cum sociis natoque penatibus et magnis dis parturient montes, nascetur ridiculus mus. Donec quam felis, ultricies nec,</p>
      <div class="location-rule"></div>
    </article>
    <article class="location" style="top:570px">
      <div class="location-photo-frame"><div class="location-photo" role="img" aria-label="Photo of clinic staff at location five"></div></div>
      <h3 class="location-title">LOCATION 05</h3>
      <p class="location-text">Lorem ipsum dolor sit amet, consectetuer adipiscing elit. Aenean commodo ligula eget dolor. Aenean massa. Cum sociis natoque penatibus et magnis dis parturient montes, nascetur ridiculus mus. Donec quam felis, ultricies nec,</p>
    </article>
  </div>

  <div class="contact-photo" role="img" aria-label="Photo of a pill bottle wrapped in a blue measuring tape on a white surface"></div>

  <div class="contact-panel">
    <div class="contact-item" style="top:18px">
      <svg viewBox="0 0 18 18" aria-hidden="true"><polygon points="1,8 17,1 11,17 8,10" fill="var(--white)"/></svg>
      <p class="note">Academy of Walk-in Clinic Practice<br>912 Larkfield Ave. Suite 418E<br>Naperville, IL 60563</p>
    </div>
    <div class="contact-item" style="top:92px">
      <svg viewBox="0 0 18 18" aria-hidden="true"><rect x="1.5" y="4" width="15" height="10" fill="none" stroke="var(--white)" stroke-width="1.4"/><polyline points="1.5,4 9,10 16.5,4" fill="none" stroke="var(--white)" stroke-width="1.4"/></svg>
      <p class="note">Info@gaphwalk.org</p>
    </div>
    <div class="contact-item phone" style="top:130px">
      <svg viewBox="0 0 18 18" aria-hidden="true"><path d="M4 1.5 L7 1.5 L8 5.5 L6 7 C7 9.5 8.5 11 11 12 L12.5 10 L16.5 11 L16.5 14 C16.5 15.5 15 16.5 13.5 16.5 C7 16 2 11 1.5 4.5 C1.5 3 2.5 1.5 4 1.5 Z" fill="var(--white)"/></svg>
      <span>1 855-431-7094</span>
    </div>
    <div class="contact-item social" style="top:174px">
      <span class="social-dot"></span><span>friendspage.net/academygaph</span>
    </div>
    <div class="contact-item social" style="top:202px">
      <span class="social-dot"></span><span>@AcademyGAPH</span>
    </div>
  </div>
</section>

</body>
</html>
```